Web-Based Software Platform - 34 Individual designs for user interface

We have a new piece of software that requires 34 individual "tiles" for a user interface. An example of the way they will be displayed is included in the file, along with examples of 34 tiles that we created in house.

There is a title associated with each tile. This is all real estate related.

image sizes needed

width: 290px
height: 218px

Target Market(s)

real estate users

Industry/Entity Type

Real Estate

Number of Pages Required

1 page

Font styles to use
Sans Serif

Colors
3176b5
fbee3d
9bcb3b
f37122

Requirements
Must have
• 34 seperate images
Nice to have
• see file
Should not have
• see file

```html
<!DOCTYPE html>
<html lang="en">
<head>
<meta charset="utf-8">
<title>Property Tiles – Version 1 Colour Combinations</title>
<link rel="stylesheet" href="https://fonts.googleapis.com/css2?family=Fira+Sans:wght@600;700&display=swap">
<style>
  :root{
    --page:#ffffff;
    --caption:#222222;
    --white:#ffffff;
  }
  *{margin:0;padding:0;box-sizing:border-box}
  html,body{width:1098px;height:1200px;overflow:hidden;background:var(--page)}
  body{position:relative;font-family:"Fira Sans",Arial,sans-serif}
  .tile-sheet{position:absolute;left:0;top:0;width:1098px;height:1200px}
  .tile{
    position:absolute;width:335px;height:252px;overflow:hidden;
    background:var(--bg);
  }
  .tile-pattern{
    position:absolute;inset:0;
    background:radial-gradient(ellipse at 50% 40%, var(--bg-hi) 0%, var(--bg) 70%, var(--bg-lo) 100%);
  }
  .orb{
    position:absolute;left:50%;top:28px;width:130px;height:130px;margin-left:-65px;border-radius:50%;
    background:
      radial-gradient(ellipse 70% 45% at 50% 22%, rgba(255,255,255,.45) 0%, rgba(255,255,255,.1) 60%, rgba(255,255,255,0) 75%),
      radial-gradient(circle at 50% 60%, var(--orb-hi) 0%, var(--orb) 75%);
    box-shadow:0 2px 4px rgba(0,0,0,.25);
  }
  .tile-title{
    position:absolute;left:6px;right:6px;top:180px;text-align:center;
    color:var(--ink);font-weight:600;font-size:21px;line-height:25px;text-transform:uppercase;
  }
  .col-1{left:18px}.col-2{left:383px}.col-3{left:749px}
  .row-1{top:22px}.row-2{top:304px}.row-3{top:584px}.row-4{top:864px}

  .green-dark {--bg:#3f8b3f;--bg-hi:#4c9a48;--bg-lo:#2f7a32;--orb:#06600a;--orb-hi:#138a16;--ink:var(--white)}
  .green-mid  {--bg:#5db65a;--bg-hi:#6cc466;--bg-lo:#4aa649;--orb:#06600a;--orb-hi:#138a16;--ink:var(--white)}
  .green-light{--bg:#9fcf97;--bg-hi:#acd8a4;--bg-lo:#8ec486;--orb:#2f9e12;--orb-hi:#5ed42a;--ink:#1f5c20}
  .red-dark   {--bg:#e06a5a;--bg-hi:#ee7b6b;--bg-lo:#d05848;--orb:#9c0d06;--orb-hi:#c7200f;--ink:#5a0f0a}
  .red-mid    {--bg:#de6555;--bg-hi:#ec7767;--bg-lo:#cf5646;--orb:#9c0d06;--orb-hi:#c7200f;--ink:#6a0e08}
  .red-light  {--bg:#eba59c;--bg-hi:#f3b5ac;--bg-lo:#e0968d;--orb:#d9321c;--orb-hi:#f35a3c;--ink:#8c1b12}
  .pink-dark  {--bg:#b87298;--bg-hi:#c680a6;--bg-lo:#a9648a;--orb:#7e0e4c;--orb-hi:#a51c68;--ink:#5a0c35}
  .pink-mid   {--bg:#c981aa;--bg-hi:#d690b7;--bg-lo:#bb739c;--orb:#7e0e4c;--orb-hi:#a51c68;--ink:#5a0c35}
  .pink-light {--bg:#bea1b2;--bg-hi:#cab0bf;--bg-lo:#b093a5;--orb:#c23c88;--orb-hi:#e35ea8;--ink:#8a1556}
  .blue-dark  {--bg:#2f5f86;--bg-hi:#386d96;--bg-lo:#265275;--orb:#083660;--orb-hi:#124a80;--ink:var(--white)}
  .blue-mid   {--bg:#3497d6;--bg-hi:#44a5e2;--bg-lo:#2888c6;--orb:#083660;--orb-hi:#124a80;--ink:#0c3a66}
  .blue-light {--bg:#7dc1ec;--bg-hi:#8dcdf3;--bg-lo:#6db3e0;--orb:#0f82d6;--orb-hi:#2aa6f2;--ink:#0c3a66}

  .sheet-caption{
    position:absolute;left:0;right:0;top:1142px;text-align:center;
    font-weight:700;font-size:27px;line-height:34px;color:var(--caption);letter-spacing:.2px;
  }
</style>
</head>
<body>
<main class="tile-sheet">
  <section class="tile green-dark col-1 row-1">
    <div class="tile-pattern" role="img" aria-label="Repeating pattern of house outlines"></div>
    <div class="orb" role="img" aria-label="Round badge with a target and cursor icon"></div>
    <p class="tile-title">Properties most likely<br>to sell</p>
  </section>
  <section class="tile green-mid col-2 row-1">
    <div class="tile-pattern" role="img" aria-label="Repeating pattern of house outlines"></div>
    <div class="orb" role="img" aria-label="Round badge with a house icon"></div>
    <p class="tile-title">Vacant properties</p>
  </section>
  <section class="tile green-light col-3 row-1">
    <div class="tile-pattern" role="img" aria-label="Repeating pattern of house outlines"></div>
    <div class="orb" role="img" aria-label="Round badge with a rising value chart icon"></div>
    <p class="tile-title">Longerproperties with<br>high equity</p>
  </section>

  <section class="tile red-dark col-1 row-2">
    <div class="tile-pattern" role="img" aria-label="Repeating pattern of house outlines"></div>
    <div class="orb" role="img" aria-label="Round badge with a target and cursor icon"></div>
    <p class="tile-title">Properties most likely<br>to sell</p>
  </section>
  <section class="tile red-mid col-2 row-2">
    <div class="tile-pattern" role="img" aria-label="Repeating pattern of house outlines"></div>
    <div class="orb" role="img" aria-label="Round badge with a house icon"></div>
    <p class="tile-title">Vacant properties</p>
  </section>
  <section class="tile red-light col-3 row-2">
    <div class="tile-pattern" role="img" aria-label="Repeating pattern of house outlines"></div>
    <div class="orb" role="img" aria-label="Round badge with a rising value chart icon"></div>
    <p class="tile-title">Longerproperties with<br>high equity</p>
  </section>

  <section class="tile pink-dark col-1 row-3">
    <div class="tile-pattern" role="img" aria-label="Repeating pattern of house outlines"></div>
    <div class="orb" role="img" aria-label="Round badge with a target and cursor icon"></div>
    <p class="tile-title">Properties most likely<br>to sell</p>
  </section>
  <section class="tile pink-mid col-2 row-3">
    <div class="tile-pattern" role="img" aria-label="Repeating pattern of house outlines"></div>
    <div class="orb" role="img" aria-label="Round badge with a house icon"></div>
    <p class="tile-title">Vacant properties</p>
  </section>
  <section class="tile pink-light col-3 row-3">
    <div class="tile-pattern" role="img" aria-label="Repeating pattern of house outlines"></div>
    <div class="orb" role="img" aria-label="Round badge with a rising value chart icon"></div>
    <p class="tile-title">Longerproperties with<br>high equity</p>
  </section>

  <section class="tile blue-dark col-1 row-4">
    <div class="tile-pattern" role="img" aria-label="Repeating pattern of house outlines"></div>
    <div class="orb" role="img" aria-label="Round badge with a target and cursor icon"></div>
    <p class="tile-title">Properties most likely<br>to sell</p>
  </section>
  <section class="tile blue-mid col-2 row-4">
    <div class="tile-pattern" role="img" aria-label="Repeating pattern of house outlines"></div>
    <div class="orb" role="img" aria-label="Round badge with a house icon"></div>
    <p class="tile-title">Vacant properties</p>
  </section>
  <section class="tile blue-light col-3 row-4">
    <div class="tile-pattern" role="img" aria-label="Repeating pattern of house outlines"></div>
    <div class="orb" role="img" aria-label="Round badge with a rising value chart icon"></div>
    <p class="tile-title">Longerproperties with<br>high equity</p>
  </section>

  <h1 class="sheet-caption">VERSION 1 WITH COLOR COMBINATIONS</h1>
</main>
</body>
</html>
```